Lantern Business Cards

Need business cards for my employees at my restaurant.

Needs to include:
Our Logo
Lantern Forks & Cellar
Name: Miriam Toddwell
Title : Owner
Address: 847 Pickering Ave. Cobalt Springs, NV 86519
Web: www.lanternkitchenbay.com
Phone: 928-555-0147
Cell: 928-555-0183
Email: info@lanternkitchenbay.com

```html
<!DOCTYPE html>
<html lang="en">
<head>
<meta charset="utf-8">
<title>Lantern Forks &amp; Cellar — Business Card</title>
<link rel="stylesheet" href="https://fonts.googleapis.com/css2?family=Poppins:wght@400;600;700&family=Libre+Baskerville:wght@700&display=swap">
<style>
  :root {
    --backdrop: #2b2b2d;
    --card: #1c1d1f;
    --red: #c8202f;
    --white: #f4f4f4;
    --rule: #8a8a8a;
    --pattern-dark: #141416;
    --pattern-light: #4a4b4e;
  }
  * { box-sizing: border-box; margin: 0; padding: 0; }
  html, body { width: 1200px; height: 1108px; overflow: hidden; }
  body {
    background: var(--backdrop);
    font-family: "Poppins", sans-serif;
    color: var(--white);
    position: relative;
  }
  .card {
    position: absolute;
    top: 234px;
    width: 400px;
    height: 640px;
    border-radius: 24px;
    background: var(--card);
    box-shadow: 0 18px 40px rgba(0,0,0,.45);
    overflow: hidden;
  }
  .card--front { left: 170px; }
  .card--back { left: 630px; }

  /* Front */
  .brand {
    position: absolute; top: 96px; left: 0; right: 0;
    display: flex; flex-direction: column; align-items: center;
  }
  .brand__dot {
    width: 92px; height: 92px; border-radius: 50%;
    background: var(--red);
    margin-bottom: 20px;
  }
  .brand__name {
    font-weight: 700; color: var(--red);
    font-size: 46px; letter-spacing: 1px; line-height: 1;
    text-transform: uppercase;
  }
  .brand__tagline {
    display: flex; align-items: center; gap: 12px;
    margin-top: 10px;
    font-weight: 400; color: var(--white);
    font-size: 14px; letter-spacing: 2px; text-transform: uppercase;
  }
  .brand__tagline::before, .brand__tagline::after {
    content: ""; width: 64px; height: 2px; background: var(--rule);
  }
  .person {
    position: absolute; top: 336px; left: 0; right: 0; text-align: center;
  }
  .person__name {
    font-family: "Libre Baskerville", serif;
    color: var(--red); font-size: 22px; letter-spacing: .5px;
    text-transform: uppercase;
  }
  .person__title { font-size: 18px; margin-top: 2px; }
  .channels {
    position: absolute; top: 408px; left: 40px; right: 40px;
    display: flex; align-items: center; gap: 10px;
  }
  .channels__rule { flex: 1; height: 1px; background: var(--rule); }
  .channels__icon {
    width: 34px; height: 34px; border-radius: 6px;
    background: var(--red);
    display: flex; align-items: center; justify-content: center;
  }
  .channels__icon svg { width: 20px; height: 20px; }
  .contact {
    position: absolute; top: 452px; left: 0; right: 0;
    text-align: center; font-size: 17px; line-height: 1.3;
    font-style: normal;
  }
  .contact__web-name { color: var(--red); }
  .contact__rule {
    width: 300px; height: 1px; background: var(--rule); margin: 12px auto;
  }

  /* Back */
  .back-pattern {
    position: absolute; inset: 0;
    background: linear-gradient(135deg, var(--pattern-dark) 20%, #2c2d30 60%, var(--pattern-light) 100%);
  }
  .back-mark {
    position: absolute; left: 262px; top: 462px;
    display: flex; align-items: center; gap: 6px;
    font-weight: 700; color: var(--red); font-size: 18px;
    text-transform: uppercase;
  }
  .back-mark__dot { width: 14px; height: 14px; border-radius: 50%; background: var(--red); }
</style>
</head>
<body>
  <section class="card card--front" aria-label="Business card front">
    <header class="brand">
      <div class="brand__dot"></div>
      <div class="brand__name">Lantern</div>
      <div class="brand__tagline">Forks &amp; Cellar</div>
    </header>

    <div class="person">
      <h1 class="person__name">Miriam Toddwell</h1>
      <p class="person__title">Owner</p>
    </div>

    <div class="channels">
      <span class="channels__rule"></span>
      <span class="channels__icon" aria-label="Phone">
        <svg viewBox="0 0 24 24" fill="#fff"><path d="M6.6 10.8a15 15 0 0 0 6.6 6.6l2.2-2.2a1 1 0 0 1 1-.25 11.4 11.4 0 0 0 3.6.57 1 1 0 0 1 1 1V20a1 1 0 0 1-1 1A17 17 0 0 1 3 4a1 1 0 0 1 1-1h3.5a1 1 0 0 1 1 1c0 1.25.2 2.45.57 3.57a1 1 0 0 1-.25 1z"/></svg>
      </span>
      <span class="channels__icon" aria-label="Mobile">
        <svg viewBox="0 0 24 24" fill="none" stroke="#fff" stroke-width="2"><rect x="7" y="2.5" width="10" height="19" rx="2"/><line x1="11" y1="18" x2="13" y2="18"/></svg>
      </span>
      <span class="channels__icon" aria-label="Email">
        <svg viewBox="0 0 24 24" fill="none" stroke="#fff" stroke-width="2"><rect x="3" y="5.5" width="18" height="13" rx="1"/><path d="M3 6l9 7 9-7"/></svg>
      </span>
      <span class="channels__icon" aria-label="Website">
        <svg viewBox="0 0 24 24" fill="none" stroke="#fff" stroke-width="2"><circle cx="12" cy="12" r="9"/><path d="M3 12h18M12 3c3 3.5 3 14.5 0 18M12 3c-3 3.5-3 14.5 0 18"/></svg>
      </span>
      <span class="channels__rule"></span>
    </div>

    <address class="contact">
      <div>928-555-0147</div>
      <div>928-555-0183</div>
      <div>info@lanternkitchenbay.com</div>
      <div>www.<span class="contact__web-name">lanternkitchenbay</span>.com</div>
      <div class="contact__rule"></div>
      <div>847 Pickering Ave.</div>
      <div>Cobalt Springs, NV 86519</div>
    </address>
  </section>

  <section class="card card--back" aria-label="Business card back">
    <div class="back-pattern" role="img" aria-label="Tonal repeating brand-mark pattern in black gloss"></div>
    <div class="back-mark"><span class="back-mark__dot"></span>Lantern</div>
  </section>
</body>
</html>
```